Coastline Haven Retreats Business Card Design

Design a business card for Coastline Haven Retreats. Look at the website for colors and reference. Card should have logo, name, title, office number, mobile number, email, URL and a tagline like, "Luxury Hotel & Resort Email Marketing" (This might change).

https://www.coastlinehavenretreats.example

The rest I will leave up to your imagination.

Contact Information for Business Card

Logo, name, title, office number, mobile number, email, URL and a tagline like, "Luxury Hotel & Resort Email Marketing" (This might change).

```html
<!DOCTYPE html>
<html lang="en">
<head>
<meta charset="utf-8">
<title>Coastline Haven Retreats – Business Card</title>
<link href="https://fonts.googleapis.com/css2?family=Montserrat:wght@700;800&family=Lato:wght@400;700&family=Dancing+Script:wght@600&display=swap" rel="stylesheet">
<style>
  :root {
    --bg: #3a3a3c;
    --orange: #f57104;
    --white: #ffffff;
    --ink: #141414;
    --grey: #555555;
    --rule: #2a2a2a;
  }
  * { box-sizing: border-box; margin: 0; padding: 0; }
  html, body { width: 1200px; height: 689px; overflow: hidden; background: var(--bg); }
  .stage { position: relative; width: 1200px; height: 689px; }
  .card {
    position: absolute; top: 196px; width: 520px; height: 297px;
    border-radius: 18px; box-shadow: 0 18px 40px rgba(0,0,0,.45);
  }
  .card-front { left: 50px; background: var(--orange); }
  .card-back { left: 630px; background: var(--white); }

  .brand {
    font-family: "Montserrat", sans-serif; font-weight: 800; color: var(--ink);
    letter-spacing: .04em; text-transform: uppercase; line-height: 1.1;
  }
  .card-front .brand {
    position: absolute; left: 0; right: 0; top: 92px; text-align: center; font-size: 30px;
  }
  .tagline {
    position: absolute; left: 0; right: 0; top: 178px; text-align: center;
    font-family: "Dancing Script", cursive; font-weight: 600; font-size: 24px; color: var(--ink);
  }

  .card-back .brand { position: absolute; right: 30px; top: 30px; font-size: 17px; text-align: right; }
  .brand-mark { display: inline-block; width: 12px; height: 12px; background: var(--orange); margin-right: 8px; vertical-align: 1px; }
  .rule-top { position: absolute; left: 30px; right: 30px; top: 78px; height: 1px; background: var(--rule); }

  .person { position: absolute; left: 30px; top: 150px; }
  .person-name { font-family: "Montserrat", sans-serif; font-weight: 700; font-size: 22px; color: var(--ink); letter-spacing: .02em; }
  .person-title { font-family: "Lato", sans-serif; font-size: 14px; color: var(--orange); margin-top: 2px; }
  .rule-mid { position: absolute; left: 30px; width: 210px; top: 204px; height: 1px; background: var(--rule); }

  .contacts { position: absolute; left: 30px; top: 214px; list-style: none; font-family: "Lato", sans-serif; font-size: 11.5px; color: var(--grey); }
  .contacts li { display: flex; align-items: center; gap: 8px; height: 17px; }
  .contacts svg { width: 10px; height: 10px; fill: var(--orange); flex: none; }

  .office { position: absolute; right: 30px; top: 98px; text-align: right; font-family: "Lato", sans-serif; font-size: 12px; color: var(--grey); line-height: 1.5; }
  .office-name { color: var(--orange); font-size: 13px; }
</style>
</head>
<body>
<main class="stage">
  <section class="card card-front">
    <div class="brand">Coastline Haven<br>Retreats</div>
    <p class="tagline">Luxury Hotel &amp; Resort Email Marketing</p>
  </section>

  <section class="card card-back">
    <div class="brand"><span class="brand-mark"></span>Coastline Haven Retreats</div>
    <div class="rule-top"></div>

    <div class="person">
      <div class="person-name">JORDAN REYES</div>
      <div class="person-title">Founder &amp; CEO</div>
    </div>
    <div class="rule-mid"></div>

    <ul class="contacts">
      <li><svg viewBox="0 0 10 10"><path d="M2 0l2 2-1 1.5c.6 1.3 1.6 2.3 3 3L7.5 5.5l2.5 2-1.5 2C4 9 1 6 .5 1.5z"/></svg>(555) 014-2290</li>
      <li><svg viewBox="0 0 10 10"><path d="M2.5 0h5v10h-5zM3.5 1v7h3V1z"/></svg>(555) 014-2291</li>
      <li><svg viewBox="0 0 10 10"><path d="M0 2h10v6H0zM.8 2.6 5 5.6l4.2-3z" fill-rule="evenodd"/></svg>info@coastlinehavenretreats.example</li>
      <li><svg viewBox="0 0 10 10"><circle cx="5" cy="5" r="5"/></svg>coastlinehavenretreats.example</li>
    </ul>

    <address class="office" style="font-style:normal">
      <div class="office-name">Coastline Haven Retreats</div>
      <div>418 Tidewater Lane, Ste 12</div>
      <div>Seabrook, CT 06999</div>
    </address>
  </section>
</main>
</body>
</html>
```